Progressive Flow Chart

Looking for a progressive flow chart centered and branching off. They all build on each other 1-3. There will be 3 different pages.

Target Market(s)

Business Owners - High Net worth Individuals

Industry/Entity Type

Finance & Business Consulting

Font styles to use
Serif

Colors
0054AA
0677BA
7BADD7
CADEEF
E8F1F8
0094D4
00A9DD
6FCCEA
C7EBF8
E9F6FB
00AB8E
00BBA5
67D7C9
C6EFE9
E9F9F6

Requirements
Nice to have
• Clean, simple, and approachable.
Should not have
• Very Busy

```html
<!DOCTYPE html>
<html lang="en">
<head>
<meta charset="utf-8">
<title>Living Trust Flow Chart</title>
<link rel="stylesheet" href="https://fonts.googleapis.com/css2?family=Poppins:wght@400;500;600;700;800&display=swap">
<style>
  :root {
    --stage: #aebfca;
    --navy-deep: #050a32;
    --navy: #0b1452;
    --ink: #0c1a4a;
    --teal: #0cf0b8;
    --sky: #2aaee2;
    --aqua: #1fd0d6;
    --white: #ffffff;
  }
  html, body {
    margin: 0;
    width: 1200px;
    height: 901px;
    overflow: hidden;
    background: var(--stage);
    font-family: "Poppins", sans-serif;
  }
  .chart {
    position: absolute;
    left: 0;
    top: 26px;
    width: 1200px;
    height: 848px;
    display: block;
  }
  .node-label { font-family: "Poppins", sans-serif; font-weight: 700; fill: var(--white); text-anchor: middle; }
  .box-title { font-family: "Poppins", sans-serif; font-weight: 700; fill: var(--ink); text-anchor: middle; font-size: 29px; }
  .box-sub { font-family: "Poppins", sans-serif; font-weight: 500; fill: var(--ink); text-anchor: middle; font-size: 22px; }
  .flow-label { font-family: "Poppins", sans-serif; font-weight: 400; fill: var(--white); font-size: 15px; }
  .badge-num { font-family: "Poppins", sans-serif; font-weight: 600; fill: var(--white); font-size: 17px; text-anchor: middle; }
  .trust-arc { font-family: "Poppins", sans-serif; font-weight: 700; fill: var(--white); font-size: 38px; letter-spacing: 9px; }
  .trustee { font-family: "Poppins", sans-serif; font-weight: 700; fill: var(--white); font-size: 34px; text-anchor: middle; }
  .brand { font-family: "Poppins", sans-serif; font-weight: 600; fill: var(--white); font-size: 30px; text-anchor: middle; }
  .flow { stroke: var(--white); stroke-width: 1.6; stroke-dasharray: 6 5; fill: none; }
  .dashed-frame { fill: none; stroke: var(--white); stroke-width: 2; stroke-dasharray: 10 7; }
  .icon-line { fill: none; stroke: var(--ink); stroke-width: 2.4; stroke-linecap: round; stroke-linejoin: round; }
</style>
</head>
<body>
<svg class="chart" viewBox="212 184 1577 1114" xmlns="http://www.w3.org/2000/svg" aria-label="Living trust flow chart">
  <defs>
    <linearGradient id="bg" x1="0" y1="0" x2="1" y2="1">
      <stop offset="0" stop-color="#0a1555"/>
      <stop offset="1" stop-color="#040828"/>
    </linearGradient>
    <radialGradient id="ornamentGlow">
      <stop offset="0" stop-color="#138c7c" stop-opacity=".28"/>
      <stop offset=".7" stop-color="#1d6fa8" stop-opacity=".14"/>
      <stop offset="1" stop-color="#1d6fa8" stop-opacity="0"/>
    </radialGradient>
    <linearGradient id="boxFill" x1="0" y1="0" x2="1" y2="0">
      <stop offset="0" stop-color="#2aaee2"/>
      <stop offset="1" stop-color="#0af2b6"/>
    </linearGradient>
    <linearGradient id="ringStroke" x1="0" y1="0" x2="1" y2="1">
      <stop offset="0" stop-color="#2a9fe6"/>
      <stop offset="1" stop-color="#0cf0b8"/>
    </linearGradient>
    <linearGradient id="trustBand" x1="0" y1="0" x2="0" y2="1">
      <stop offset="0" stop-color="#14a38c"/>
      <stop offset="1" stop-color="#1b5f9c"/>
    </linearGradient>
    <marker id="arrow" viewBox="0 0 10 10" refX="5" refY="5" markerWidth="9" markerHeight="9" orient="auto-start-reverse">
      <path d="M0,0 L10,5 L0,10 Z" fill="var(--aqua)"/>
    </marker>
    <path id="trustArc" d="M 782 735 A 220 220 0 0 1 1222 735"/>
  </defs>

  <!-- background -->
  <rect x="212" y="184" width="1577" height="1114" fill="url(#bg)"/>
  <g class="ornament" role="img" aria-label="Decorative glowing concentric rings">
    <circle cx="320" cy="285" r="160" fill="url(#ornamentGlow)"/>
  </g>
  <g class="ornament" role="img" aria-label="Decorative glowing concentric rings">
    <circle cx="1755" cy="730" r="195" fill="url(#ornamentGlow)"/>
  </g>

  <!-- brand -->
  <g class="brand-mark">
    <circle cx="1650" cy="300" r="40" fill="none" stroke="var(--white)" stroke-width="6"/>
    <text class="brand" x="1650" y="383">Orvane</text>
  </g>

  <!-- satellite nodes -->
  <g class="satellite">
    <circle cx="640" cy="447" r="92" fill="none" stroke="var(--white)" stroke-width="2" stroke-dasharray="7 5"/>
    <circle cx="640" cy="447" r="74" fill="var(--navy-deep)" stroke="url(#ringStroke)" stroke-width="8"/>
    <text class="node-label" x="640" y="458" font-size="30">CRT</text>
    <circle cx="640" cy="532" r="19" fill="var(--navy-deep)" stroke="var(--white)" stroke-width="2"/>
    <text class="badge-num" x="640" y="538">5</text>
  </g>
  <g class="satellite">
    <circle cx="1000" cy="350" r="92" fill="none" stroke="var(--white)" stroke-width="2" stroke-dasharray="7 5"/>
    <circle cx="1000" cy="350" r="74" fill="var(--navy-deep)" stroke="url(#ringStroke)" stroke-width="8"/>
    <text class="node-label" x="1000" y="361" font-size="30">DAF</text>
    <circle cx="1001" cy="430" r="19" fill="var(--navy-deep)" stroke="var(--white)" stroke-width="2"/>
    <text class="badge-num" x="1001" y="436">3</text>
  </g>
  <g class="satellite">
    <circle cx="1360" cy="447" r="92" fill="none" stroke="var(--white)" stroke-width="2" stroke-dasharray="7 5"/>
    <circle cx="1360" cy="447" r="74" fill="var(--navy-deep)" stroke="url(#ringStroke)" stroke-width="8"/>
    <text class="node-label" x="1360" y="443" font-size="28">GRAT’S</text>
    <text class="node-label" x="1360" y="479" font-size="28">IDGTS’</text>
    <circle cx="1367" cy="532" r="19" fill="var(--navy-deep)" stroke="var(--white)" stroke-width="2"/>
    <text class="badge-num" x="1367" y="538">3</text>
  </g>

  <!-- flows -->
  <g class="flows">
    <line class="flow" x1="737" y1="765" x2="660" y2="765" marker-end="url(#arrow)"/>
    <text class="flow-label" x="677" y="759">Invest</text>
    <line class="flow" x1="449" y1="1015" x2="449" y2="872" marker-end="url(#arrow)"/>
    <text class="flow-label" transform="translate(442 985) rotate(-90)">Interest</text>
    <line class="flow" x1="484" y1="872" x2="484" y2="1006" marker-end="url(#arrow)"/>
    <text class="flow-label" transform="translate(481 975) rotate(-90)">Investment</text>
    <line class="flow" x1="766" y1="862" x2="488" y2="1000" marker-end="url(#arrow)"/>
    <path d="M684 904 l12 -10 -2 14 z" fill="var(--aqua)"/>
    <text class="flow-label" transform="translate(522 976) rotate(-26)">Income</text>
    <line class="flow" x1="497" y1="870" x2="928" y2="1048" marker-end="url(#arrow)"/>
    <line class="flow" x1="1060" y1="1058" x2="1060" y2="1002" marker-end="url(#arrow)"/>
    <text class="flow-label" x="1067" y="1039">Income</text>
    <line class="flow" x1="830" y1="1143" x2="667" y2="1143" marker-end="url(#arrow)"/>
    <text class="flow-label" x="728" y="1137">Rent</text>
    <line class="flow" x1="1230" y1="882" x2="1435" y2="1055"/>
    <path d="M1346 983 l-2 -14 -10 8 z" fill="var(--aqua)"/>
    <line class="flow" x1="1480" y1="1012" x2="1255" y2="822"/>
    <path d="M1360 910 l4 12 9 -9 z" fill="var(--aqua)"/>
  </g>

  <!-- living trust -->
  <g class="living-trust">
    <circle cx="1000" cy="735" r="268" fill="none" stroke="var(--aqua)" stroke-width="2" stroke-dasharray="7 5"/>
    <circle cx="1000" cy="735" r="242" fill="url(#trustBand)"/>
    <circle cx="1000" cy="735" r="184" fill="#0d1648" stroke="url(#ringStroke)" stroke-width="6"/>
    <text class="trust-arc"><textPath href="#trustArc" startOffset="50%" text-anchor="middle">LIVING TRUST</textPath></text>
    <text class="trustee" x="998" y="808">YOU</text>
    <text class="trustee" x="1000" y="848">TRUSTEE</text>
    <circle cx="1001" cy="488" r="19" fill="var(--navy-deep)" stroke="var(--white)" stroke-width="2"/>
    <text class="badge-num" x="1001" y="494">1</text>
  </g>

  <!-- entity boxes -->
  <g class="entity bank">
    <rect x="320" y="690" width="335" height="172" rx="22" fill="url(#boxFill)"/>
    <rect x="336" y="706" width="303" height="140" rx="16" class="dashed-frame"/>
    <circle cx="480" cy="690" r="46" fill="var(--navy-deep)"/>
    <circle cx="480" cy="690" r="40" fill="var(--white)"/>
    <g class="icon-line">
      <path d="M458 680 L480 668 L502 680 Z"/><path d="M462 684 v20 M472 684 v20 M488 684 v20 M498 684 v20 M456 708 h48"/>
    </g>
    <text class="box-title" x="483" y="771">BANK</text>
    <text class="box-sub" x="480" y="798">Makes investments in</text>
    <text class="box-sub" x="482" y="825">real estate+ Business</text>
    <circle cx="476" cy="857" r="19" fill="var(--navy-deep)" stroke="var(--white)" stroke-width="2"/>
    <text class="badge-num" x="476" y="863">2</text>
  </g>

  <g class="entity real-estate">
    <rect x="318" y="1062" width="336" height="170" rx="22" fill="url(#boxFill)"/>
    <rect x="334" y="1078" width="304" height="138" rx="16" class="dashed-frame"/>
    <circle cx="481" cy="1063" r="46" fill="var(--navy-deep)"/>
    <circle cx="481" cy="1063" r="40" fill="var(--white)"/>
    <g class="icon-line">
      <rect x="458" y="1050" width="16" height="30"/><rect x="474" y="1042" width="20" height="38"/>
      <circle cx="492" cy="1078" r="11" fill="var(--white)"/><path d="M492 1072 v12"/>
    </g>
    <text class="box-title" x="483" y="1154">REAL ESTATE</text>
    <text class="box-sub" x="483" y="1181">LLC</text>
    <circle cx="480" cy="1229" r="19" fill="var(--navy-deep)" stroke="var(--white)" stroke-width="2"/>
    <text class="badge-num" x="480" y="1235">1</text>
  </g>

  <g class="entity business">
    <rect x="832" y="1062" width="335" height="170" rx="22" fill="url(#boxFill)"/>
    <rect x="848" y="1078" width="303" height="138" rx="16" class="dashed-frame"/>
    <circle cx="1000" cy="1063" r="46" fill="var(--navy-deep)"/>
    <circle cx="1000" cy="1063" r="40" fill="var(--white)"/>
    <g class="icon-line">
      <rect x="984" y="1066" width="34" height="22" rx="3"/><path d="M994 1066 v-6 h14 v6 M984 1076 h34"/>
      <path d="M978 1044 h18 M978 1052 h14"/>
    </g>
    <text class="box-title" x="1002" y="1141">BUSINESS</text>
    <text class="box-sub" x="1002" y="1168">LLC-member/manager</text>
    <text class="box-sub" x="1002" y="1195">corp-president</text>
    <circle cx="1006" cy="1229" r="19" fill="var(--navy-deep)" stroke="var(--white)" stroke-width="2"/>
    <text class="badge-num" x="1006" y="1235">1</text>
  </g>

  <g class="entity insurance">
    <rect x="1323" y="1062" width="336" height="170" rx="22" fill="url(#boxFill)"/>
    <rect x="1339" y="1078" width="304" height="138" rx="16" class="dashed-frame"/>
    <circle cx="1488" cy="1063" r="46" fill="var(--navy-deep)"/>
    <circle cx="1488" cy="1063" r="40" fill="var(--white)"/>
    <g class="icon-line">
      <rect x="1466" y="1044" width="30" height="40" rx="3"/>
      <path d="M1472 1056 l3 3 5 -5 M1472 1068 l3 3 5 -5 M1484 1057 h6 M1484 1069 h6"/>
      <path d="M1500 1058 l10 4 v8 c0 6 -5 10 -10 12 c-5 -2 -10 -6 -10 -12 v-8 z" fill="var(--white)"/>
    </g>
    <text class="box-title" x="1488" y="1159">INSURANCE</text>
    <circle cx="1488" cy="1229" r="19" fill="var(--navy-deep)" stroke="var(--white)" stroke-width="2"/>
    <text class="badge-num" x="1488" y="1235">2</text>
  </g>
</svg>
</body>
</html>
```